Bref créative
Businesscard + stationary
outstand and cretive master piece!
Bright & Fun-filled
Mariana Tolvaldi
www.pixelharbor-exemplo.com.br
contato@pixelharbor-exemplo.com.br
You need to add to business card:
Skype: pixelharbor.online
Twitter: @PixelHarboron
Secondary text to go below logo: Desenvolvimento Web
On the back of business card goes only the logo and some nice art if applyable
This is the new website layout, so please follow this style to create the businesscard and stationary.
This is teh original logo file in EPS
this is another version of teh logo

```html
<!DOCTYPE html>
<html lang="pt-BR">
<head>
<meta charset="utf-8">
<title>pixelharbor — papelaria</title>
<link rel="stylesheet" href="https://fonts.googleapis.com/css2?family=Comfortaa:wght@700&family=Open+Sans:wght@400;600&display=swap">
<style>
  :root{
    --blue:#4ba3de;
    --ink:#2c2c2e;
    --paper:#ffffff;
    --stage:#e6e7e9;
    --muted:#6b6b6b;
    --light:#ffffff;
  }
  *{box-sizing:border-box;margin:0;padding:0}
  html,body{width:1200px;height:818px;overflow:hidden}
  body{background:var(--stage);font-family:"Open Sans",sans-serif;position:relative}
  .piece{position:absolute;box-shadow:0 3px 10px rgba(0,0,0,.18)}
  .brand{font-family:"Comfortaa",sans-serif;font-weight:700;letter-spacing:-.5px;line-height:1}
  .tagline{font-size:9px;line-height:1.2}
  .band{position:absolute;left:0;width:100%}
  .band svg{display:block;width:100%;height:100%}
  .contacts{list-style:none;font-size:8px;line-height:1.45}
  .contacts li{display:flex;align-items:center;gap:5px;white-space:nowrap}
  .contacts li::before{content:"";width:6px;height:6px;border-radius:50%;background:var(--blue);flex:none}

  /* business card front */
  .card-front{left:202px;top:72px;width:250px;height:148px;background:var(--ink);color:var(--light)}
  .card-front .logo{position:absolute;left:16px;top:18px}
  .card-front .brand{font-size:25px;color:var(--light)}
  .card-front .tagline{color:#d7d7d7;margin-left:40px}
  .card-front .band{top:66px;height:22px}
  .card-front .name{position:absolute;left:118px;top:70px;font-size:10px;font-weight:600;color:var(--light)}
  .card-front .contacts{position:absolute;left:118px;top:94px;color:#dcdcdc;font-size:6.5px}

  /* business card back */
  .card-back{left:336px;top:240px;width:262px;height:146px;background:var(--blue);color:var(--light)}
  .card-back .logo{position:absolute;left:34px;top:34px}
  .card-back .brand{font-size:32px;color:var(--light)}
  .card-back .tagline{font-size:11px;margin-left:70px}
  .card-back .social{position:absolute;left:40px;bottom:12px;display:flex;gap:26px;font-size:7px}

  /* envelopes */
  .envelope{width:460px;height:200px;background:var(--paper);overflow:hidden}
  .envelope .flap{position:absolute;left:0;top:0;width:100%;height:64px}
  .envelope .flap svg{width:100%;height:100%;display:block}
  .envelope .flap-logo{position:absolute;left:50%;top:12px;transform:translateX(-50%);text-align:center}
  .envelope .flap-logo .brand{font-size:15px;color:var(--light)}
  .envelope .logo{position:absolute;left:18px;top:82px}
  .envelope .logo .brand{font-size:26px;color:var(--ink)}
  .envelope .logo .tagline{color:var(--muted);margin-left:46px}
  .envelope .band{bottom:26px;height:20px}
  .envelope-back{left:72px;top:456px}
  .envelope-back .logo{top:70px;left:16px}
  .envelope-back .logo .brand{font-size:20px}
  .envelope-back .logo .tagline{font-size:8px;margin-left:34px}
  .envelope-front{left:178px;top:572px}

  /* letterhead */
  .letterhead{left:648px;top:110px;width:444px;height:586px;background:var(--paper)}
  .letterhead .logo{position:absolute;left:18px;top:42px}
  .letterhead .brand{font-size:30px;color:var(--ink)}
  .letterhead .tagline{color:var(--muted);font-size:10px;margin-left:54px}
  .letterhead .band{top:500px;height:22px}
  .letterhead .contacts{position:absolute;left:34px;top:528px;color:var(--muted);font-size:7px}
</style>
</head>
<body>

<section class="piece card-front" aria-label="Cartão de visita, frente">
  <div class="logo">
    <div class="brand">pixelharbor</div>
    <div class="tagline">Desenvolvimento Web</div>
  </div>
  <div class="band">
    <svg viewBox="0 0 250 22" preserveAspectRatio="none">
      <rect x="100" y="2" width="150" height="18" fill="var(--blue)"/>
      <line x1="0" y1="18.5" x2="100" y2="18.5" stroke="var(--blue)" stroke-width="3"/>
    </svg>
  </div>
  <p class="name">Mariana Tolvaldi</p>
  <ul class="contacts">
    <li>11 5550 0142</li>
    <li>11 5550 0187</li>
    <li>contato@pixelharbor-exemplo.com.br</li>
    <li>www.pixelharbor-exemplo.com.br</li>
  </ul>
</section>

<section class="piece card-back" aria-label="Cartão de visita, verso">
  <div class="logo">
    <div class="brand">pixelharbor</div>
    <div class="tagline">Desenvolvimento Web</div>
  </div>
  <div class="social">
    <span>Skype: pixelharbor.online</span>
    <span>Twitter: @PixelHarboron</span>
  </div>
</section>

<section class="piece envelope envelope-back" aria-label="Envelope com aba escura">
  <div class="flap">
    <svg viewBox="0 0 460 64" preserveAspectRatio="none">
      <path d="M0 0 H460 V20 Q230 80 0 20 Z" fill="var(--ink)"/>
    </svg>
  </div>
  <div class="flap-logo"><div class="brand">pixelharbor</div></div>
  <div class="logo">
    <div class="brand">pixelharbor</div>
    <div class="tagline">Desenvolvimento Web</div>
  </div>
  <div class="band">
    <svg viewBox="0 0 460 20" preserveAspectRatio="none">
      <line x1="0" y1="17" x2="460" y2="17" stroke="var(--blue)" stroke-width="4"/>
    </svg>
  </div>
</section>

<section class="piece envelope envelope-front" aria-label="Envelope com aba azul">
  <div class="flap">
    <svg viewBox="0 0 460 64" preserveAspectRatio="none">
      <path d="M0 0 H460 V20 Q230 80 0 20 Z" fill="var(--blue)"/>
    </svg>
  </div>
  <div class="flap-logo"><div class="brand">pixelharbor</div></div>
  <div class="logo">
    <div class="brand">pixelharbor</div>
    <div class="tagline">Desenvolvimento Web</div>
  </div>
  <div class="band">
    <svg viewBox="0 0 460 20" preserveAspectRatio="none">
      <line x1="0" y1="17" x2="460" y2="17" stroke="var(--blue)" stroke-width="4"/>
    </svg>
  </div>
</section>

<section class="piece letterhead" aria-label="Papel timbrado">
  <div class="logo">
    <div class="brand">pixelharbor</div>
    <div class="tagline">Desenvolvimento Web</div>
  </div>
  <div class="band">
    <svg viewBox="0 0 444 22" preserveAspectRatio="none">
      <line x1="0" y1="19" x2="444" y2="19" stroke="var(--blue)" stroke-width="4"/>
    </svg>
  </div>
  <ul class="contacts">
    <li>11 5550 0142</li>
    <li>11 5550 0187</li>
    <li>contato@pixelharbor-exemplo.com.br</li>
    <li>www.pixelharbor-exemplo.com.br</li>
  </ul>
</section>

</body>
</html>
```